Pretzel Company needs a Pretzel Bag Design for Retail

Harlow Twists, a smoked, seasoned pretzel maker, needs an eye popping pretzel package design that will make consumers excited to try their smoked, seasoned pretzels

```html
<!DOCTYPE html>
<html lang="en">
<head>
<meta charset="utf-8">
<title>Harlow Twists – Pretzel Bag</title>
<link href="https://fonts.googleapis.com/css2?family=Arimo:wght@400;700&display=swap" rel="stylesheet">
<style>
:root{
  --navy:#1e4279;
  --white:#ffffff;
  --ink:#000000;
  --red:#ee1111;
  --pretzel:#d08a45;
  --icon:#e6ebf3;
}
*{margin:0;padding:0;box-sizing:border-box}
html,body{width:730px;height:1200px;overflow:hidden;background:var(--navy)}
.bag{position:relative;width:730px;height:1200px;background:var(--navy);color:var(--white);font-family:"Arimo",Arial,sans-serif}
.brand-name{position:absolute;left:0;width:730px;top:218px;text-align:center;font-size:62px;font-weight:700;color:var(--white);letter-spacing:1px}
.intro{position:absolute;left:86px;width:320px}
.company{top:348px;font-size:17.5px;white-space:nowrap}
.company small{font-size:15px;font-weight:700}
.copy{font-size:13px;line-height:16px}
.copy p+p{margin-top:16px}
.story-1{top:386px}
.pretzel-art{position:absolute;left:182px;top:538px;width:78px;height:70px;border-radius:40%;background:radial-gradient(circle at 50% 45%,#e2a562,var(--pretzel) 70%,#b06f32)}
.history-title{position:absolute;left:86px;top:637px;font-size:17px;font-weight:400}
.story-2{top:672px;width:320px}
.panel{position:absolute;left:455px;top:351px;width:189px;height:473px;background:var(--white);color:var(--ink)}
.facts{position:absolute;left:12px;top:9px;width:165px;height:281px;border:1px solid var(--ink);padding:1px 2px;font-size:7px;line-height:1}
.facts .title{font-size:18.5px;font-weight:700;height:20px;border-bottom:1px solid var(--ink);letter-spacing:.2px}
.facts .servings{height:10px;font-size:8.5px;padding-top:1px}
.facts .size{height:11px;font-size:8.5px;font-weight:700;display:flex;justify-content:space-between}
.bar-thick{height:7px;background:var(--ink)}
.amount{height:6px;font-size:5px;font-weight:700;padding-top:1px}
.calories{height:22px;display:flex;justify-content:space-between;align-items:flex-end;border-bottom:3px solid var(--ink);font-weight:700}
.calories span:first-child{font-size:14px}
.calories span:last-child{font-size:21px}
.dv{height:10px;text-align:right;font-size:5.5px;font-weight:700;padding-top:2px;border-bottom:1px solid var(--ink)}
.row{height:11.7px;display:flex;justify-content:space-between;align-items:center;border-bottom:1px solid var(--ink)}
.row b{font-weight:700}
.row.in1{padding-left:9px}
.row.in2{padding-left:18px}
.row.last{border-bottom:none}
.row.vit{height:10.5px;font-size:6.8px}
.row.vit.end{border-bottom:2px solid var(--ink)}
.note{font-size:4.8px;line-height:6.8px;padding:2px 4px 0}
.ingredients{position:absolute;left:15px;top:299px;width:168px;font-size:8.7px;line-height:10.4px}
.rule{position:absolute;left:184px;top:873px;width:363px;height:4px;background:var(--red)}
.tagline{position:absolute;left:86px;width:558px;top:903px;text-align:center;font-size:16.5px;line-height:19.6px;font-weight:400}
.social{position:absolute;left:0;width:730px;top:1049px;display:flex;justify-content:center;gap:9px}
.social span{width:18px;height:18px;border-radius:50%;background:var(--icon)}
.follow{position:absolute;left:0;width:730px;top:1074px;text-align:center;font-size:13px}
</style>
</head>
<body>
<main class="bag">
  <div class="brand-name">Harlow</div>

  <h2 class="intro company">Harlow Twists - <small>Prairie Oven LLC</small></h2>
  <div class="intro copy story-1">
    <p>My pretzels are Seasoned and slow smoked to perfection. Born in a bar and named after my dad!</p>
    <p>The most common reaction from people is the texture of them, not too crunchy not too soft, the perfect crunch that almost melts in your mouth. The flavor is described as unique with the perfect amount of smoke.</p>
  </div>

  <div class="pretzel-art" role="img" aria-label="Illustration of a golden baked pretzel"></div>

  <h3 class="history-title">History:</h3>
  <div class="intro copy story-2">
    <p>Created in 2020 in a bar as a snack to serve to our customers while they drank beer. When we decided to close the doors because of the distance we lived from the bar.&nbsp; After we closed, our customers would contact me for my pretzels because they couldnt stop craving them. that is when i got the idea to start making them on a bigger scale and selling them. long story short they have really become a hit and currently in the process of mass production.</p>
  </div>

  <section class="panel">
    <div class="facts">
      <div class="title">Nutrition Facts</div>
      <div class="servings">12 servings per container</div>
      <div class="size"><span>Serving size</span><span>15 pretzels (28g)</span></div>
      <div class="bar-thick"></div>
      <div class="amount">Amount per serving</div>
      <div class="calories"><span>Calories</span><span>130</span></div>
      <div class="dv">% Daily Value*</div>
      <div class="row"><span><b>Total Fat</b> 7g</span><b>9%</b></div>
      <div class="row in1"><span>Saturated Fat 1g</span><b>4%</b></div>
      <div class="row in1"><span><i>Trans</i> Fat 0g</span></div>
      <div class="row"><span><b>Cholesterol</b> 0mg</span><b>0%</b></div>
      <div class="row"><span><b>Sodium</b> 350mg</span><b>15%</b></div>
      <div class="row"><span><b>Total Carbohydrate</b> 17g</span><b>6%</b></div>
      <div class="row in1"><span>Dietary Fiber 0g</span><b>0%</b></div>
      <div class="row in1"><span>Total Sugars 0g</span></div>
      <div class="row in2"><span>Includes 0g Added Sugars</span><b>0%</b></div>
      <div class="row last"><span><b>Protein</b> 2g</span></div>
      <div class="bar-thick"></div>
      <div class="row vit"><span>Vitamin D 0mcg</span><span>0%</span></div>
      <div class="row vit"><span>Calcium 0mg</span><span>0%</span></div>
      <div class="row vit"><span>Iron 1mg</span><span>4%</span></div>
      <div class="row vit end"><span>Potassium 0mg</span><span>0%</span></div>
      <div class="note">* The % Daily Value (DV) tells you how much a nutrient in a serving of food contributes to a daily diet. 2,000 calories a day is used for general nutrition advice.</div>
    </div>
    <p class="ingredients">INGREDIENTS: Pretzels (Wheat Flour, Salt, Vegetable Oil [Corn, Sunflower or Canola], Malt Syrup [Derived from Corn and Malt Barley], Yeast, Baking Soda); Soybean Oil, Artificial Flavor, Beta Carotene (for Color); Seasoning (Maltodextrin, Buttermilk, Salt, Monosodium Glutamate, Garlic, Onion, Lactic Acid, Calcium Lactate, Citric Acid,Paprika, Chili Pepper, Less Than 2% of Vinegar, Red Bell Pepper, Calcium Silicate, Artificial Flavor, Xanthan Gum, Carboxymethlcellulose, Guar Gum, Natural Flavor); Cayenne Pepper, Silicon Dioxide (to Prevent Cracking)<br>CONTAINS: WHEAT, SOY, MILK</p>
  </section>

  <div class="rule"></div>

  <p class="tagline">Take your snack game to the next level with Harlow's Twists! Each golden-brown twist is infused with a rich smoky flavor and finished off with a dash of sea salt, creating a mouthwatering combination of savory goodness. Crunchy, bold, and absolutely irresistible!</p>

  <div class="social" aria-label="Social channels"><span></span><span></span><span></span><span></span></div>
  <p class="follow">FOLLOW US</p>
</main>
</body>
</html>
```